Business Card Design Project for Investment Fund

Veloria Capital Management is an emerging wealth management firm based in New Jersey. It offers superior investment returns to high net worth individuals and institutions by finding undervalued assets.
We recently selected a company logo which was inspired by the Tucana constellation. Beta Tucanae is a group of six stars, containing star cluster 47 Tucanae, rated the second brightest object in the sky.
Now we need a business card design. Since we are an investment firm, the design should project a sense of stability, growth and professionalism. The owner is interested in something simple yet striking, which of course is consistent with the logo.
Wealthy individuals, probably middle aged or older, in the US
Investment

```html
<!DOCTYPE html>
<html lang="en">
<head>
<meta charset="utf-8">
<title>Veloria Capital Management – Business Card</title>
<link rel="stylesheet" href="https://fonts.googleapis.com/css2?family=Open+Sans:wght@400;600;700&display=swap">
<style>
  :root {
    --backdrop: #2b2b2b;
    --card-dark: #2e3a42;
    --card-light: #ffffff;
    --mark-dark-text: #dfe3e6;
    --brand-ink: #2e3a42;
    --text-grey: #5a5f63;
    --text-body: #3c4043;
    --divider: #8a8f93;
    --mark-square: #26307a;
  }
  * { box-sizing: border-box; margin: 0; padding: 0; }
  html, body {
    width: 1200px; height: 900px; overflow: hidden;
    background: var(--backdrop);
    font-family: "Open Sans", Arial, sans-serif;
  }
  .canvas { position: relative; width: 1200px; height: 900px; }

  .card {
    position: absolute; top: 308px;
    width: 513px; height: 285px; border-radius: 20px;
  }
  .card--front { left: 73px; background: var(--card-dark); }
  .card--back  { left: 616px; background: var(--card-light); }

  /* Front */
  .front-name {
    position: absolute; left: 0; right: 0; top: 104px;
    text-align: center; color: var(--mark-dark-text); font-weight: 600;
  }
  .front-name .line-main { display: block; font-size: 38px; letter-spacing: 5px; line-height: 44px; }
  .front-name .line-sub  { display: block; font-size: 22px; line-height: 28px; }

  /* Back: brand column */
  .brand-square {
    position: absolute; left: 83px; top: 69px;
    width: 88px; height: 88px; border-radius: 9px; background: var(--mark-square);
  }
  .brand-name {
    position: absolute; left: 0; width: 254px; top: 170px;
    text-align: center; color: var(--brand-ink); font-weight: 600;
  }
  .brand-name .line-main { display: block; font-size: 30px; letter-spacing: 4px; line-height: 34px; }
  .brand-name .line-sub  { display: block; font-size: 16px; line-height: 22px; }

  .divider {
    position: absolute; left: 250px; top: 57px;
    width: 1px; height: 170px; background: var(--divider);
  }

  /* Back: contact column */
  .contact { position: absolute; left: 273px; top: 60px; color: var(--text-body); }
  .person-name { font-size: 21px; color: var(--text-grey); line-height: 28px; }
  .person-title { font-size: 15px; color: var(--text-grey); line-height: 20px; margin-bottom: 14px; }
  .detail { display: flex; align-items: flex-start; font-size: 12.5px; line-height: 16px; }
  .detail svg { width: 11px; height: 11px; margin: 2px 7px 0 0; flex: none; fill: var(--text-body); }
  .detail--gap { margin-top: 16px; }
</style>
</head>
<body>
<main class="canvas">
  <section class="card card--front" aria-label="Card front">
    <p class="front-name"><span class="line-main">VELORIA</span><span class="line-sub">Capital Management</span></p>
  </section>

  <section class="card card--back" aria-label="Card back">
    <div class="brand-square"></div>
    <p class="brand-name"><span class="line-main">VELORIA</span><span class="line-sub">Capital Management</span></p>
    <div class="divider"></div>

    <div class="contact">
      <p class="person-name">Daniel Hartley</p>
      <p class="person-title">CEO</p>

      <div class="detail">
        <svg viewBox="0 0 12 12"><path d="M6 0a4 4 0 0 0-4 4c0 3 4 8 4 8s4-5 4-8a4 4 0 0 0-4-4zm0 5.6A1.6 1.6 0 1 1 6 2.4a1.6 1.6 0 0 1 0 3.2z"/></svg>
        <span>48 Harbor Ave.<br>Newark, NJ 07102</span>
      </div>
      <div class="detail">
        <svg viewBox="0 0 12 12"><path d="M2.6 0.8l1.6 2.4-1 1.1c.6 1.6 1.9 2.9 3.5 3.5l1.1-1 2.4 1.6-.9 2C5.4 10.3 1.7 6.6 0.6 1.7z"/></svg>
        <span>973-555-0142</span>
      </div>

      <div class="detail detail--gap">
        <svg viewBox="0 0 12 12"><path d="M0 2.5h12v7H0z M0.6 3l5.4 3.6L11.4 3" fill="none" stroke="#3c4043" stroke-width="1"/></svg>
        <span>dhartley@veloriacapmgmt.com</span>
      </div>
      <div class="detail">
        <svg viewBox="0 0 12 12"><g fill="none" stroke="#3c4043" stroke-width="1"><circle cx="6" cy="6" r="5.3"/><ellipse cx="6" cy="6" rx="2.3" ry="5.3"/><path d="M0.7 6h10.6M1.6 3.3h8.8M1.6 8.7h8.8"/></g></svg>
        <span>www.veloriacapmgmt.com</span>
      </div>
    </div>
  </section>
</main>
</body>
</html>
```